Website Design for Harbor Trade Exchange! Buying Electronics Antiques Gold and valuables Online w/Cash

Our company gives people a reliable place to sell their old or un-needed valuables online where they can get a fair price and be involved in the decision upon the price to be paid. We provide prices for a huge variety of items ranging from Cell Phones, El

```html
<!DOCTYPE html>
<html lang="en">
<head>
<meta charset="utf-8">
<title>Harbor Trade Exchange</title>
<link href="https://fonts.googleapis.com/css2?family=PT+Sans+Narrow:wght@400;700&family=Arimo:wght@400;700&display=swap" rel="stylesheet">
<style>
:root{
  --blue:#2b4fa8;
  --blue-dark:#1e3f93;
  --blue-light:#3f6bd0;
  --red:#d3242b;
  --ink:#333;
  --muted:#666;
  --line:#d6d6d6;
  --panel:#f4f4f4;
  --white:#fff;
  --green:#8fae1b;
}
*{box-sizing:border-box;margin:0;padding:0}
html,body{width:969px;height:1200px;overflow:hidden;background:var(--white)}
.canvas{position:relative;width:969px;height:1200px;overflow:hidden;font-family:"Arimo",Arial,sans-serif;color:var(--ink)}
.abs{position:absolute}
.cond{font-family:"PT Sans Narrow","Arial Narrow",sans-serif}

.brand{left:0;width:969px;top:62px;text-align:center;font-family:"PT Sans Narrow",sans-serif;font-weight:700;font-size:46px;color:var(--blue)}
.brand-mark{display:inline-block;width:22px;height:22px;border-radius:50%;background:var(--red);margin-right:12px;vertical-align:middle;position:relative;top:-4px}

.nav{top:177px;left:117px;display:flex;gap:0}
.nav a{font-family:"PT Sans Narrow",sans-serif;font-size:14px;color:#777;text-decoration:none;height:23px;line-height:23px;margin-right:28px}
.nav a.active{background:var(--blue);color:var(--white);padding:0 11px;border-radius:3px;position:relative}
.nav a.active::after{content:"";position:absolute;left:14px;bottom:-6px;border:6px solid transparent;border-top-color:var(--blue);border-bottom:0}

.hero{top:223px;left:0;width:969px;height:212px;background:radial-gradient(ellipse at 60% 40%,var(--blue-light),var(--blue-dark) 75%)}
.hero-figure{left:156px;top:3px;width:156px;height:209px;border-radius:40px 40px 10px 10px;background:linear-gradient(180deg,#e9eef8,#b8c6e6)}
.hero h1{left:361px;top:33px;font-family:"PT Sans Narrow",sans-serif;font-weight:700;font-size:44px;color:var(--white);letter-spacing:.2px;white-space:nowrap;text-shadow:0 2px 3px rgba(0,0,0,.25)}
.hero p{left:361px;top:95px;width:476px;font-size:10px;line-height:14px;color:#dfe6f7;text-align:justify}
.select{left:368px;top:153px;width:286px;height:30px;background:var(--white);border-radius:3px;border:1px solid #c8c8c8;font-family:"PT Sans Narrow",sans-serif;font-size:15px;color:#666;line-height:28px;padding-left:12px}
.select svg{position:absolute;right:10px;top:10px}
.quote-btn{left:675px;top:153px;width:143px;height:30px;border-radius:5px;background:linear-gradient(#fff,#dcdcdc);font-family:"PT Sans Narrow",sans-serif;font-size:15px;color:#333;line-height:30px;padding-left:16px;box-shadow:0 1px 2px rgba(0,0,0,.3)}
.quote-btn svg{position:absolute;right:14px;top:11px}

.steps{top:480px;left:118px;width:719px;height:127px;border:1px solid var(--line);background:linear-gradient(#fff,#f1f1f1)}
.step h2{font-family:"PT Sans Narrow",sans-serif;font-weight:700;font-size:22px;color:var(--red);white-space:nowrap}
.step p{font-size:10px;line-height:11px;color:#444;margin-top:12px}
.step-icon{border-radius:8px}

.main{top:636px;left:118px;width:720px;height:470px;border:1px solid var(--line);background:linear-gradient(#fff 60%,#f3f3f3);box-shadow:0 4px 6px rgba(0,0,0,.08)}
.heading{font-family:"PT Sans Narrow",sans-serif;font-weight:700;font-size:16px;color:var(--red);white-space:nowrap}
.box{border:1px solid var(--line);background:var(--panel)}
.field{height:22px;border:1px solid #d8d8d8;background:var(--white);font-size:10px;font-style:italic;color:#aaa;line-height:20px;padding-left:9px}
.small{font-size:10px;line-height:13px;color:#444}

.tab{top:781px;height:34px;border:1px solid var(--line);border-bottom:0;border-radius:3px 3px 0 0;background:linear-gradient(#fff,#ececec);font-family:"PT Sans Narrow",sans-serif;font-size:16px;color:#888;text-align:center;line-height:34px}
.tab.active{background:var(--white);color:#444;height:35px}
.products{left:364px;top:814px;width:460px;height:150px;border:1px solid var(--line);background:var(--white)}
.product{top:14px;width:99px;height:105px;border:1px solid var(--line);background:var(--white)}
.product .shot{position:absolute;left:18px;top:8px;width:62px;height:88px;border-radius:6px}
.product-name{top:132px;width:99px;text-align:center;font-family:"PT Sans Narrow",sans-serif;font-size:17px;color:#444}

.quote-text{font-size:10px;line-height:13px;color:#444;width:185px}
.quote-by{font-size:10px;font-weight:700;color:#333}
.quote-by span{color:var(--green)}

.footer{top:1154px;left:0;width:969px;height:46px;background:var(--blue);color:#e6ecfa;font-size:10px;line-height:40px}
.social{width:16px;height:16px;border-radius:2px;top:1120px}
</style>
</head>
<body>
<div class="canvas">

  <div class="abs brand"><span class="brand-mark"></span>Harbor Trade Exchange</div>

  <nav class="abs nav">
    <a class="active" href="#">HOME</a>
    <a href="#">ABOUT US</a>
    <a href="#">OUR SERVICES</a>
    <a href="#">REGISTER / LOGIN</a>
    <a href="#">CONTACT US</a>
  </nav>

  <section class="abs hero">
    <div class="abs hero-figure" role="img" aria-label="Cartoon professor mascot holding cash and a money bag"></div>
    <h1 class="abs">SELL YOUR PRODUCT FOR CASH</h1>
    <p class="abs">Lorem ipsum dolor sit amet, consectetur adipiscing elit. Pellentesque pellentesque nibh a lacus semper sceleris-que. Nam euismod libero mollis enim mollis vitae convallis neque ultrices. Praesent convallis tincidunt elit, imperdiet dapibus ante laoreet id.</p>
    <div class="abs select">-- Select your categorie --
      <svg width="12" height="10" viewBox="0 0 12 10"><path d="M0 0h12L6 10z" fill="#222"/></svg>
    </div>
    <div class="abs quote-btn">REQUEST A QUOTE
      <svg width="8" height="9" viewBox="0 0 8 9"><path d="M0 0l8 4.5L0 9z" fill="#333"/></svg>
    </div>
  </section>

  <section class="abs steps">
    <svg class="abs" style="left:204px;top:-1px" width="40" height="127" viewBox="0 0 40 127"><path d="M2 0l34 63.5L2 127" fill="none" stroke="#d4d4d4" stroke-width="2"/><path d="M9 0l34 63.5L9 127" fill="none" stroke="#fff" stroke-width="2"/></svg>
    <svg class="abs" style="left:466px;top:-1px" width="40" height="127" viewBox="0 0 40 127"><path d="M2 0l34 63.5L2 127" fill="none" stroke="#d4d4d4" stroke-width="2"/><path d="M9 0l34 63.5L9 127" fill="none" stroke="#fff" stroke-width="2"/></svg>

    <div class="abs step" style="left:14px;top:18px">
      <h2>1- GET A QUOTE</h2>
      <p>Lorem ipsum<br>dolor sit amet, con-<br>sectetur adipiscing<br>elit.</p>
    </div>
    <div class="abs step-icon" style="left:140px;top:20px;width:54px;height:87px;background:linear-gradient(#e2474b,#c51d23)" role="img" aria-label="Pointing hand icon"></div>

    <div class="abs step" style="left:265px;top:18px">
      <h2>2- SHIP PACKAGE</h2>
      <p>Lorem ipsum<br>dolor sit amet, consecte-<br>tur adipiscing elit.</p>
    </div>
    <div class="abs step-icon" style="left:379px;top:45px;width:70px;height:69px;background:linear-gradient(#f1dc9a,#d4b563)" role="img" aria-label="Cardboard shipping box"></div>

    <div class="abs step" style="left:521px;top:18px">
      <h2>3- GET PAID</h2>
      <p>Lorem ipsum<br>dolor sit amet, con-<br>sectetur adipiscing<br>elit.</p>
    </div>
    <div class="abs step-icon" style="left:625px;top:50px;width:84px;height:57px;background:linear-gradient(#a8d08a,#6ea653)" role="img" aria-label="Banknotes and gold coins"></div>
  </section>

  <section class="abs main"></section>

  <!-- Left column -->
  <h3 class="abs heading" style="left:132px;top:653px">NEWSLETTER SIGN UP</h3>
  <div class="abs box" style="left:132px;top:682px;width:200px;height:80px"></div>
  <div class="abs" style="left:145px;top:689px;width:35px;height:35px;border-radius:4px;background:linear-gradient(#f2f2f2,#c9cfd8)" role="img" aria-label="Envelope with pen icon"></div>
  <p class="abs small" style="left:186px;top:694px;width:142px">Please enter your email address to recieve our <b>free newsletter</b></p>
  <div class="abs" style="left:143px;top:732px;width:131px;height:18px;border:1px solid #ccc;background:#fff"></div>
  <div class="abs" style="left:273px;top:732px;width:51px;height:18px;background:var(--blue);color:#fff;font-size:10px;font-weight:700;text-align:center;line-height:18px">Submit</div>

  <h3 class="abs heading" style="left:132px;top:779px">ASK FOR PRICE</h3>
  <div class="abs box" style="left:132px;top:808px;width:200px;height:161px"></div>
  <p class="abs small" style="left:144px;top:817px">Please enter your product informations</p>
  <div class="abs field" style="left:142px;top:837px;width:179px">Your name ...</div>
  <div class="abs field" style="left:142px;top:871px;width:179px">Your email ...</div>
  <div class="abs field" style="left:142px;top:901px;width:179px">Your product description ...</div>
  <div class="abs cond" style="left:151px;top:935px;width:161px;height:24px;border-radius:5px;background:linear-gradient(#fff,#dadada);box-shadow:0 1px 2px rgba(0,0,0,.3);text-align:center;line-height:24px;font-size:15px;color:#333">GET INSTANT QUOTE</div>

  <h3 class="abs heading" style="left:132px;top:980px">CALL US NOW</h3>
  <div class="abs box" style="left:132px;top:1006px;width:200px;height:83px"></div>
  <svg class="abs" style="left:141px;top:1014px" width="37" height="36" viewBox="0 0 37 36">
    <rect x="1" y="1" width="10" height="34" rx="3" fill="#e4e4e4" stroke="#999"/>
    <rect x="11" y="6" width="25" height="29" rx="3" fill="#efefef" stroke="#999"/>
    <rect x="15" y="10" width="17" height="6" fill="#bfc6d2"/>
    <g fill="#888"><rect x="15" y="19" width="4" height="3"/><rect x="21.5" y="19" width="4" height="3"/><rect x="28" y="19" width="4" height="3"/><rect x="15" y="24" width="4" height="3"/><rect x="21.5" y="24" width="4" height="3"/><rect x="28" y="24" width="4" height="3"/><rect x="15" y="29" width="4" height="3"/><rect x="21.5" y="29" width="4" height="3"/><rect x="28" y="29" width="4" height="3"/></g>
  </svg>
  <div class="abs" style="left:185px;top:1022px;font-size:16px;font-weight:700;color:var(--blue-dark)">+030 60 555 0142</div>
  <p class="abs small" style="left:141px;top:1056px;width:190px;font-size:9.5px">Give your online business a competitive edge. <b>Call Us Today for Free Instant Quote</b></p>

  <!-- Right column -->
  <h3 class="abs heading" style="left:363px;top:653px">WHO WE ARE</h3>
  <p class="abs small" style="left:363px;top:680px;width:462px;text-align:justify;line-height:14px">Lorem ipsum dolor sit amet, consectetur adipiscing elit. <b>Lorem Lorem ipsum</b> dolor. Lorem ipsum dolor sit amet, consectetur adipiscing elit. Lorem ipsum dolor.Lorem ipsum dolor sit amet, consectetur adipiscing elit. Lorem Lorem ipsum dolor.Lorem ipsum dolor sit amet, consectetur adipiscing elit. Lorem Lorem ipsum dolor.Lorem ipsum dolor sit amet, consectetur adipiscing elit. <b>Lorem Lorem ipsum</b> dolor. dolor.</p>

  <h3 class="abs heading" style="left:363px;top:753px">BROWSE CATEGORIES</h3>
  <div class="abs tab active" style="left:364px;width:101px">Cell Phones</div>
  <div class="abs tab" style="left:477px;width:86px">Electronics</div>
  <div class="abs tab" style="left:574px;width:99px">Laptops</div>
  <div class="abs tab" style="left:678px;width:97px">Antiques</div>
  <div class="abs tab" style="left:784px;width:40px"><svg style="margin-top:9px" width="12" height="16" viewBox="0 0 12 16"><path d="M2 1l8 7-8 7" fill="none" stroke="#777" stroke-width="2"/></svg></div>

  <div class="abs products">
    <svg class="abs" style="left:5px;top:52px" width="10" height="34" viewBox="0 0 10 34"><path d="M9 1L1 17l8 16" fill="none" stroke="#777" stroke-width="1.5"/></svg>
    <svg class="abs" style="left:445px;top:52px" width="10" height="34" viewBox="0 0 10 34"><path d="M1 1l8 16-8 16" fill="none" stroke="#777" stroke-width="1.5"/></svg>
    <div class="abs product" style="left:17px"><div class="shot" role="img" aria-label="Compact orange music player" style="background:linear-gradient(#f09a3a,#c8661c)"></div></div>
    <div class="abs product" style="left:125px"><div class="shot" role="img" aria-label="Classic music player with click wheel" style="background:linear-gradient(#e8e8e8,#9a9a9a)"></div></div>
    <div class="abs product" style="left:231px"><div class="shot" role="img" aria-label="Touchscreen music player" style="background:linear-gradient(#555,#111)"></div></div>
    <div class="abs product" style="left:339px"><div class="shot" role="img" aria-label="Small clip music player" style="background:linear-gradient(#d6d6d6,#8a8a8a)"></div></div>
    <div class="abs product-name" style="left:17px">Tunebox Mini</div>
    <div class="abs product-name" style="left:125px">Tunebox Classic</div>
    <div class="abs product-name" style="left:231px">Tunebox Touch</div>
    <div class="abs product-name" style="left:339px">Tunebox Clip</div>
  </div>

  <h3 class="abs heading" style="left:367px;top:980px">CLIENT TESTIMONIALS</h3>
  <div class="abs" style="left:367px;top:1009px;width:457px;height:84px;border:1px solid var(--line);background:var(--white)"></div>
  <div class="abs" style="left:591px;top:1020px;width:1px;height:62px;background:var(--line)"></div>
  <p class="abs quote-text" style="left:385px;top:1023px">Es hat uns einen Riesenspaß gemacht mit euch zusammen zu arbeiten.</p>
  <p class="abs quote-text" style="left:623px;top:1023px">Es hat uns einen Riesenspaß gemacht mit euch zusammen zu arbeiten.</p>
  <svg class="abs" style="left:536px;top:1036px" width="24" height="20" viewBox="0 0 24 20"><path d="M2 0h8v9L6 20H2l3-10H2zM14 0h8v9l-4 11h-4l3-10h-3z" fill="#ccc"/></svg>
  <svg class="abs" style="left:774px;top:1036px" width="24" height="20" viewBox="0 0 24 20"><path d="M2 0h8v9L6 20H2l3-10H2zM14 0h8v9l-4 11h-4l3-10h-3z" fill="#ccc"/></svg>
  <p class="abs quote-by" style="left:385px;top:1061px">Jonas Weber, <span>Brightline</span></p>
  <p class="abs quote-by" style="left:623px;top:1061px">Jonas Weber, <span>Brightline</span></p>

  <!-- Live chat row -->
  <svg class="abs" style="left:118px;top:1119px" width="24" height="22" viewBox="0 0 24 22"><rect x="1" y="1" width="19" height="14" rx="2" fill="#e8ecf4" stroke="#8a97b3"/><path d="M5 15v5l5-5" fill="#e8ecf4" stroke="#8a97b3"/><circle cx="19" cy="16" r="4.5" fill="#f2a22b"/></svg>
  <div class="abs cond" style="left:146px;top:1120px;font-weight:700;font-size:16px;color:var(--blue)">LIVE CHAT</div>
  <div class="abs cond" style="left:216px;top:1122px;font-size:12px;color:#333">Live help is available from 9:00 AM to 6:00 PM Monday to Friday</div>
  <div class="abs cond" style="left:710px;top:1121px;font-size:12px;color:#333">Connect With Us</div>
  <div class="abs social" style="left:784px;background:#3b5a9a"></div>
  <div class="abs social" style="left:803px;background:#c4302b"></div>
  <div class="abs social" style="left:822px;background:#f08a24"></div>

  <footer class="abs footer">
    <span class="abs" style="left:118px;top:0">Copyright © harbortrade. 2012. All Right Reserved</span>
    <span class="abs" style="right:129px;top:0">Home &nbsp;| About Us | Our Services | Our People | Request An Audit | Contact Us</span>
  </footer>

</div>
</body>
</html>
```